OLU58 biz card & Stationery

LU58 is a personalized shopping experience brought to you, that lets you find and discover fashion goods through a collection of boutiques curated by taste-makers - celebrities, stylists, designers, and fashion bloggers. Boutiques uses visual technology to help fashionistas discover and shop their look and creates the opportunity for designers to showcase their collections and latest inspirations online.

OLU58 is built on technology developed by our team of fashion experts who work with engineers to “teach” our computer systems to understand various patterns, pairings, and genre definitions. When signed into your account, OLU58 learns about your style and preferences and in turn, provides you better results and recommendations over time. Ultimately, OLU58 will provide shoppers with a much richer and interactive shopping experience and help drive traffic to retailers' websites.

We need a definitely cool business card. The card must be black! And must use our official logo which can be download from OLU58.com

The address for Letter head and evenlop, please use 4872 Crestwick Parkway, Sutie 510 Los Angeles CA90412, email will be anyone@OLU58.com, website is www.OLU58.com

thanks

We received some of the design, thanks. But most of the design are not what we want. We need a very clean version with black ground, you may also use some dark gray to add the element. please take a look at http://morvalstudio.no/work/#pelter__ostrama/, we do like this kind of design very much. hope it help.

```html
<!DOCTYPE html>
<html lang="en">
<head>
<meta charset="utf-8">
<title>OLU58 business cards &amp; stationery</title>
<link rel="stylesheet" href="https://fonts.googleapis.com/css2?family=Tenor+Sans&display=swap">
<style>
  :root {
    --backdrop: #f4f4f4;
    --paper: #ffffff;
    --paper-edge: #d6d6d6;
    --band-light: #e6e6e6;
    --envelope: #f0f0f0;
    --charcoal: #383735;
    --black: #000000;
    --logo-grey: #bdbdbd;
    --logo-mid: #7a7a7a;
    --url-grey: #c4c4c4;
    --ink: #555555;
    --ink-light: #e2e2e2;
    --ink-dark: #111111;
  }
  * { box-sizing: border-box; margin: 0; padding: 0; }
  html, body { width: 1200px; height: 884px; overflow: hidden; }
  body {
    background: var(--backdrop);
    font-family: "Tenor Sans", sans-serif;
    position: relative;
  }
  .wordmark { font-weight: 400; line-height: 1; letter-spacing: 0.5px; position: absolute; }
  .address { position: absolute; font-size: 6.5px; line-height: 8px; white-space: nowrap; }
  .vertical {
    position: absolute;
    writing-mode: vertical-rl;
    transform: rotate(180deg);
    white-space: nowrap;
    line-height: 1;
  }

  /* Letterhead */
  .letterhead {
    position: absolute; left: 203px; top: 41px; width: 588px; height: 761px;
    background: var(--paper); border: 1px solid var(--paper-edge);
  }
  .letterhead__band {
    position: absolute; left: 0; top: 19px; width: 100%; height: 69px;
    background: var(--band-light);
  }
  .letterhead .wordmark { left: 437px; top: 25px; font-size: 37px; color: var(--logo-grey); }
  .letterhead .address { left: 475px; top: 58px; color: var(--ink); }
  .letterhead__site { left: 552px; bottom: 26px; font-size: 24px; color: var(--url-grey); letter-spacing: 0.5px; }
  .letterhead__site small { font-size: 10px; margin-inline-start: 6px; letter-spacing: 0; }

  /* Envelope */
  .envelope {
    position: absolute; left: 544px; top: 214px; width: 598px; height: 256px;
    background: var(--envelope); border: 1px solid var(--paper-edge);
  }
  .envelope__band {
    position: absolute; left: 0; top: 20px; width: 100%; height: 70px;
    background: var(--charcoal);
  }
  .envelope .wordmark { left: 431px; top: 26px; font-size: 37px; color: var(--logo-mid); }
  .envelope .address { left: 470px; top: 61px; color: var(--ink-light); }
  .envelope__site {
    position: absolute; left: 21px; bottom: 10px; font-size: 24px; color: var(--url-grey);
    white-space: nowrap; letter-spacing: 0.5px;
  }
  .envelope__site small { font-size: 8px; letter-spacing: 0; }

  /* Business cards */
  .card {
    position: absolute; width: 137px; height: 243px;
    transform: rotate(-9deg); overflow: hidden;
  }
  .card--back { left: 102px; top: 421px; background: var(--black); }
  .card--front { left: 246px; top: 399px; background: var(--charcoal); }

  .card--back .vertical { right: 6px; bottom: 48px; color: var(--ink-light); font-size: 19px; }
  .card--back .vertical span { display: block; }
  .card--back .tagline { font-size: 13px; color: #6a6a6a; padding-inline-start: 70px; }

  .card--front .wordmark { left: 7px; top: 4px; font-size: 36px; color: var(--logo-mid); }
  .card--front .address { left: 41px; top: 38px; font-size: 6px; line-height: 7px; color: var(--ink-light); }
  .card--front .vertical { left: 9px; bottom: 17px; font-size: 18px; color: var(--ink-dark); }
</style>
</head>
<body>

  <section class="letterhead" aria-label="Letterhead">
    <div class="letterhead__band"></div>
    <div class="wordmark">OLU58</div>
    <p class="address">4872 Crestwick Parkway<br>Sutie 510 Los Angeles CA90412<br>email anyone@OLU58.com</p>
    <p class="vertical letterhead__site">www.OLU58.com<small>social fashion online</small></p>
  </section>

  <section class="envelope" aria-label="Envelope">
    <div class="envelope__band"></div>
    <div class="wordmark">OLU58</div>
    <p class="address">4872 Crestwick Parkway<br>Sutie 510 Los Angeles CA90412<br>email anyone@OLU58.com</p>
    <p class="envelope__site">www.OLU58.com <small>social fashion online</small></p>
  </section>

  <section class="card card--back" aria-label="Business card back">
    <p class="vertical"><span class="tagline">social fashion online</span><span>www.OLU58.com</span></p>
  </section>

  <section class="card card--front" aria-label="Business card front">
    <div class="wordmark">OLU58</div>
    <p class="address">4872 Crestwick Parkway<br>Sutie 510 Los Angeles CA90412<br>email anyone@OLU58.com</p>
    <p class="vertical">www.OLU58.com</p>
  </section>

</body>
</html>
```